Carrowby Ridge 2013 Vintage Cuvee

We need a label design for a 2013 Vintage Cuvee bottle, which is a premium sparkling white wine.

About Carrowby Ridge Wine (for your information):
Grown in the cool climate GI (Geographical Indicator) of Denmark, WESTERN AUSTRALIA, in the Great Southern the Carrowby Ridge vineyard is located in gravelly loam soil amidst tall Jarrah and Marri trees.

Finished label product must:
• Comply with Australian labelling requirements (see attached shiraz example)
• Fit on the face of standard sparkling wine bottle (exact bottle to be used TBA)
• Use the Carrowby Ridge logo (attached)
• Be clean, modern, and high end design
• See suitable for commercial printing

Please use the attached reserve label as a GUIDE only for your design. Foil closure colour is not determined, designers can use creativity to come up with a stylish new label. the glass colour is green, so this may change your colour scheme choices.

Will provide finalised wording details once we have received the tasting notes from the winemakers but would like to start seeing designs and colour schemes for this

Target Market(s)

Wine drinkers 25-60

Requirements
Must have
• Logo
• Name of wine- 2013 Vintage Cuvee

```html
<!DOCTYPE html>
<html lang="en">
<head>
<meta charset="utf-8">
<title>Carrowby Ridge 2013 Vintage Cuvee Label</title>
<link rel="stylesheet" href="https://fonts.googleapis.com/css2?family=Josefin+Sans:wght@700&display=swap">
<style>
  :root {
    --page: #ffffff;
    --label-grey: #d1d3d4;
    --lime: #c4d12e;
    --lime-soft: #dfe48f;
    --pale-wine: #f4f6dc;
    --ink: #231f20;
    --white: #ffffff;
  }
  html, body {
    margin: 0;
    padding: 0;
    width: 1200px;
    height: 1200px;
    overflow: hidden;
    background: var(--page);
  }
  .canvas {
    position: relative;
    width: 1200px;
    height: 1200px;
    background: var(--page);
  }
  .label {
    position: absolute;
    left: 45px;
    top: 108px;
    width: 1110px;
    height: 984px;
    background: var(--label-grey);
    overflow: hidden;
  }
  .label-art {
    position: absolute;
    inset: 0;
    width: 100%;
    height: 100%;
  }
  .vintage-year,
  .wine-name {
    font-family: "Josefin Sans", sans-serif;
    font-weight: 700;
  }
  .vintage-year { fill: var(--white); }
  .wine-name { fill: var(--ink); }
  .brand {
    position: absolute;
    left: 720px;
    top: 880px;
    display: flex;
    align-items: center;
    gap: 12px;
    font-family: "Josefin Sans", sans-serif;
    font-weight: 700;
    font-size: 34px;
    letter-spacing: 1px;
    color: var(--ink);
  }
  .brand-dot {
    width: 16px;
    height: 16px;
    border-radius: 50%;
    background: var(--ink);
  }
</style>
</head>
<body>
  <main class="canvas">
    <section class="label">
      <svg class="label-art" viewBox="0 0 1110 984" xmlns="http://www.w3.org/2000/svg">
        <defs>
          <linearGradient id="bubble-spray" x1="0" y1="0" x2="0" y2="1">
            <stop offset="0" stop-color="var(--lime)"/>
            <stop offset="1" stop-color="var(--lime-soft)"/>
          </linearGradient>
        </defs>
        <g class="sparkle-illustration" role="img" aria-label="Lime green bubbles rising in a widening spray from a glass of sparkling white wine">
          <path d="M216 0 L866 0 L668 575 L528 575 Z" fill="url(#bubble-spray)" opacity="0.85"/>
          <rect x="505" y="575" width="190" height="409" rx="40" fill="var(--pale-wine)"/>
        </g>
        <text class="vintage-year" x="411" y="238" font-size="150" textLength="288" lengthAdjust="spacingAndGlyphs">2013</text>
        <text class="wine-name" x="46" y="425" font-size="152" textLength="1011" lengthAdjust="spacingAndGlyphs">VINTAGE CUVEE</text>
      </svg>
      <div class="brand"><span class="brand-dot"></span>Carrowby Ridge</div>
    </section>
  </main>
</body>
</html>
```